Cellar Crew Poster / Flyer Ad Design

We need a poster design (and a complimentary A6 flyer) to promote our Adult Rock Band Course called 'Cellar Crew'.

Target market is adults aged 25 - 50 primarily

Design to be eye catching, creative, appealing and easy to understand. Most of the distribution will be street marketing, email marketing, social media, music magazines and websites and to other music teachers.

We need the design to be as an A3 and A4 poster and an A6 promo flyer/e-flyer. Should look good in colour and we'll want a version in black and white.

Would be good to also incorporate our music school logo (just for branding purposes).

Text as follows:

CELLAR CREW
The Ultimate Rock Band Course for Adults

Ever wondered what it would be like to play in a band?

Feeling musically rusty and looking for a way to start playing your instrument again?

Then here’s an exciting opportunity you can’t miss!

All musical levels
Beginner/Intermediate to Advanced Players

Limited Numbers

REGISTER ONLINE NOW
www.tunewellstudio.com.au

Starts Saturday 3rd August
Newtown

Over 6 exciting weekends you’ll work with one of our experienced professional band coaches and transform yourselves into the ultimate ‘Cellar Crew’

Discover how to play in a band
Revisit your musical abilities
Practice songs
Perform on Stage

Drummers, Bass Guitarists, Singers, Keys, Guitarists, Saxophone, Percussionists and others all welcome to join

For more information, course costs and registration, please visit www.tunewellstudio.com.au or call 02 7391 4825 / 0438 572 904

Reason: Hi Everyone, I've been away and unable to respond to some of the designs because I've been ill. Have decided to extend the deadline and now commit to paying designers. Look forward to seeing more designs. Any questions, please let me know. Thanks Melinda

```html
<!DOCTYPE html>
<html lang="en">
<head>
<meta charset="utf-8">
<title>Cellar Crew – The Ultimate Rock Band Course for Adults</title>
<link rel="stylesheet" href="https://fonts.googleapis.com/css2?family=Anton&family=Oswald:wght@500;600;700&family=Ubuntu:wght@700&display=swap">
<style>
  :root {
    --ink-dark: #140604;
    --fire-deep: #5a0e06;
    --fire-red: #b3250c;
    --fire-orange: #e5641a;
    --fire-glow: #f7b049;
    --banner: #ef7a23;
    --banner-text: #fde7b0;
    --white: #ffffff;
    --teal: #5cc4cf;
    --hot-orange: #f5661b;
    --cap-orange: #f39a1a;
    --footer: #0b0b0b;
  }
  * { margin: 0; padding: 0; box-sizing: border-box; }
  html, body { width: 851px; height: 1200px; overflow: hidden; background: var(--ink-dark); }
  .poster {
    position: relative;
    width: 851px;
    height: 1200px;
    overflow: hidden;
    background:
      radial-gradient(ellipse 55% 40% at 62% 38%, var(--fire-glow) 0%, var(--fire-orange) 35%, transparent 75%),
      radial-gradient(ellipse 90% 70% at 50% 50%, var(--fire-red) 0%, var(--fire-deep) 65%, var(--ink-dark) 100%);
    font-family: "Oswald", sans-serif;
    color: var(--white);
  }
  .stage-photo {
    position: absolute;
    left: 130px; top: 185px;
    width: 690px; height: 820px;
    border-radius: 40% 40% 30% 30%;
    background: radial-gradient(ellipse at 50% 55%, rgba(20,8,6,0.85) 0%, rgba(40,14,8,0.6) 45%, transparent 75%);
  }
  .title {
    position: absolute; top: 6px; left: 0; width: 100%;
    text-align: center;
    font-family: "Anton", sans-serif; font-weight: 400;
    font-size: 118px; line-height: 1;
    letter-spacing: 4px;
    text-shadow: 3px 4px 6px rgba(0,0,0,0.6);
  }
  .subtitle-band {
    position: absolute; top: 124px; left: 25px;
    width: 801px; height: 40px;
    background: var(--banner);
    box-shadow: 0 2px 6px rgba(0,0,0,0.4);
    display: flex; align-items: center; justify-content: center;
    font-family: "Ubuntu", sans-serif; font-weight: 700;
    font-size: 37px; line-height: 1; color: var(--banner-text);
    text-shadow: 1px 1px 2px rgba(120,40,0,0.7);
    white-space: nowrap;
  }
  .start-date {
    position: absolute; top: 172px; left: 0; width: 851px;
    text-align: center;
    font-family: "Ubuntu", sans-serif; font-weight: 700;
    font-size: 25px; line-height: 30px;
  }
  .shadowed { text-shadow: 2px 2px 3px rgba(0,0,0,0.85); }
  .intro {
    position: absolute; top: 266px; left: 5px; width: 380px;
    text-align: center;
    font-weight: 700; font-size: 29px; line-height: 36px;
  }
  .intro .big-six {
    font-family: "Anton", sans-serif; font-weight: 400; color: var(--hot-orange);
    font-size: 82px; line-height: 36px; vertical-align: -4px;
  }
  .intro .crew-name {
    display: block; margin-top: 4px;
    color: var(--hot-orange); font-size: 40px; line-height: 42px; font-weight: 700;
  }
  .pitch {
    position: absolute; top: 494px; left: 25px; width: 440px;
    color: var(--teal);
    font-weight: 700; font-size: 30px; line-height: 36px;
    letter-spacing: 0.4px;
  }
  .pitch p { margin-bottom: 40px; }
  .drop-cap {
    font-family: "Anton", sans-serif; font-weight: 400;
    letter-spacing: 0;
  }
  .drop-cap.e { color: var(--cap-orange); font-size: 92px; line-height: 86px; }
  .discover {
    position: absolute; top: 214px; left: 478px; width: 362px;
    text-align: center;
    font-weight: 700; font-size: 25px; line-height: 30px;
  }
  .drop-cap.d { color: var(--teal); font-size: 100px; line-height: 86px; }
  .discover ul { list-style: none; }
  .instruments {
    position: absolute; top: 396px; left: 472px; width: 370px;
    text-align: center;
    font-weight: 700; font-size: 24px; line-height: 29px;
  }
  .school-name {
    position: absolute; top: 902px; left: 380px; width: 260px;
    text-align: center;
    font-weight: 700; font-size: 28px; line-height: 40px;
    color: var(--white);
  }
  .register {
    position: absolute; top: 1036px; left: 444px; width: 400px;
    text-align: center;
  }
  .register .cta { font-family: "Anton", sans-serif; font-weight: 400; font-size: 47px; line-height: 58px; white-space: nowrap; }
  .register .url { font-weight: 700; font-size: 28px; line-height: 36px; letter-spacing: 0.8px; }
  .footer {
    position: absolute; bottom: 0; left: 0; width: 851px; height: 52px;
    background: var(--footer);
    display: flex; align-items: center; justify-content: center;
    font-weight: 500; font-size: 15.5px; white-space: nowrap;
  }
</style>
</head>
<body>
<main class="poster">
  <div class="stage-photo" role="img" aria-label="Silhouettes of a rock band on a glowing stage behind a black drum kit with cymbals"></div>

  <h1 class="title">CELLAR CREW</h1>
  <div class="subtitle-band">The Ultimate Rock Band Course for Adults</div>
  <p class="start-date shadowed">Starts Saturday 3rd August Newtown</p>

  <p class="intro shadowed">
    Over <span class="big-six">6</span> exciting weekends<br>
    you’ll work with one of our<br>
    experienced professional<br>
    band coaches and transform<br>
    yourselves into the ultimate
    <span class="crew-name">‘Cellar Crew’</span>
  </p>

  <div class="pitch shadowed">
    <p><span class="drop-cap e">E</span>ver wondered what it<br>would be like to play in<br>a band?</p>
    <p>Feeling musically rusty<br>and looking for a way to start<br>playing your instrument again?</p>
    <p>Then here’s an exciting<br>opportunity you can’t miss!</p>
    <p>All musical levels<br>Beginner/Intermediate to<br>Advanced Players</p>
    <p>Limited Numbers</p>
  </div>

  <div class="discover shadowed">
    <p><span class="drop-cap d">D</span>iscover how to play in a band</p>
    <ul>
      <li>Revisit your musical abilities</li>
      <li>Practice songs</li>
      <li>Perform on Stage</li>
    </ul>
  </div>

  <p class="instruments shadowed">
    Drummers, Bass Guitarists, Singers,<br>
    Keys, Guitarists, Saxophone,<br>
    Percussionists and others<br>
    all welcome to join
  </p>

  <p class="school-name">Tunewell Studio</p>

  <div class="register shadowed">
    <p class="cta">REGISTER ONLINE NOW</p>
    <p class="url">www.tunewellstudio.com.au</p>
  </div>

  <footer class="footer">For more information, course costs and registration, please visit www.tunewellstudio.com.au or call 02 7391 4825 / 0438 572 904</footer>
</main>
</body>
</html>
```